Small soho-London based IT Support company website

We've had our logo and stationary redesigned on Sketch Harbor and now we'd like our website done.
We're a small IT support company. Our client base is mainly design studios and advertising agencies working mainly on Zobs.
As such our website needs to be young clean and professional looking.
Our current site can be viewed at http://orvane-lux.it
We currently use Joomla but we're happy to move to Wordpress if that's the only option.

```html
<!DOCTYPE html>
<html lang="en">
<head>
<meta charset="utf-8">
<title>Orvane Lux – IT Support in Soho</title>
<link href="https://fonts.googleapis.com/css2?family=PT+Sans:wght@400;700&family=Ubuntu:wght@300;400;500&display=swap" rel="stylesheet">
<style>
:root{
  --dark:#2f2f2f;
  --lime:#a8cc1c;
  --lime-deep:#8db000;
  --lime-band-top:#b5d92a;
  --lime-band-bottom:#7ea800;
  --text:#555;
  --rule:#e6e6e6;
  --paper:#f5f4f0;
  --white:#fff;
}
*{box-sizing:border-box;margin:0;padding:0}
html,body{width:1100px;height:1200px;overflow:hidden;background:var(--white)}
body{position:relative;font-family:"Ubuntu",sans-serif;color:var(--text)}

/* header */
.site-header{position:absolute;left:0;top:0;width:1100px;height:114px;background:linear-gradient(#262626,#4a4a4a)}
.brand{position:absolute;left:72px;top:24px;display:flex;align-items:center;gap:12px;font-family:"PT Sans",sans-serif;font-weight:700;font-size:60px;color:var(--lime);line-height:1}
.brand-dot{width:20px;height:20px;border-radius:50%;background:var(--lime)}
.callout{position:absolute;left:864px;top:2px;color:#ddd;font-family:"Ubuntu",sans-serif;font-weight:300}
.callout-icon{position:absolute;left:0;top:0;width:32px;height:32px;border-radius:50%;background:radial-gradient(circle at 40% 35%,#c9ec3a,#6f9a00)}
.callout-label{position:absolute;left:41px;top:4px;font-size:22px;white-space:nowrap}
.callout-phone{position:absolute;left:6px;top:31px;font-size:23px;white-space:nowrap}
.main-nav{position:absolute;top:82px;left:0;width:1100px;height:32px}
.main-nav a{position:absolute;top:0;height:32px;line-height:34px;color:#fff;font-family:"PT Sans",sans-serif;font-weight:700;font-size:12px;text-decoration:none;text-align:center}
.main-nav a.active{background:var(--lime);border-radius:3px 3px 0 0}

/* hero */
.hero{position:absolute;left:0;top:114px;width:1100px;height:307px;background:linear-gradient(180deg,var(--lime-band-top),var(--lime-band-bottom))}
.hero-frame{position:absolute;left:57px;top:10px;width:648px;height:282px;background:#fff;border-radius:6px;padding:5px;box-shadow:0 1px 3px rgba(0,0,0,.25)}
.hero-photo{width:100%;height:100%;border-radius:4px;background:linear-gradient(100deg,#f4f4f4 0%,#cfd3d6 45%,#eef0f2 70%,#aeb6bd 100%)}
.hero-title{position:absolute;left:715px;top:28px;font-family:"PT Sans",sans-serif;font-weight:700;font-size:44px;color:#111}
.hero-copy{position:absolute;left:717px;top:96px;width:314px;color:#fff;font-size:12px;line-height:20px;text-align:justify}
.btn-more{position:absolute;left:721px;top:259px;width:105px;height:32px;border-radius:16px;background:linear-gradient(#fff,#d8d8d8);color:#444;font-family:"PT Sans",sans-serif;font-weight:700;font-size:15px;text-align:center;line-height:32px}
.hero-rule{position:absolute;left:0;top:432px;width:1100px;height:5px;background:var(--rule)}

/* services */
.service{position:absolute;top:436px;width:313px;height:383px;border:3px solid #eee;border-top:none;background:#fff}
.service-head{position:absolute;left:35px;top:11px;width:265px;height:31px;border-radius:16px;background:linear-gradient(#5a5a5a,#1f1f1f);color:#fff;font-family:"Ubuntu",sans-serif;font-weight:400;font-size:21px;line-height:31px;padding-left:24px}
.service-icon{position:absolute;left:4px;top:2px;width:44px;height:44px;border-radius:50%}
.service-photo{position:absolute;left:10px;top:57px;width:288px;height:115px;border:1px solid #ccc;padding:4px;background:#fff}
.service-photo div{width:100%;height:100%;background:linear-gradient(90deg,#f7f7f7,#cfcfcf 50%,#f7f7f7)}
.service-copy{position:absolute;left:10px;top:178px;width:288px;font-size:11px;line-height:18px;text-align:justify;letter-spacing:.3px}
.service-list{list-style:none;margin-top:6px}
.service-list li{position:relative;padding-left:14px}
.service-list li::before{content:"";position:absolute;left:1px;top:6px;border-left:4px solid #555;border-top:3px solid transparent;border-bottom:3px solid transparent}

/* location */
.location{position:absolute;left:63px;top:838px;width:644px;height:301px;background:var(--paper);border:1px solid #e2e0da;border-radius:8px}
.map{position:absolute;left:17px;top:17px;width:352px;height:270px;border:2px solid #fff;box-shadow:0 0 0 1px #ddd;background:linear-gradient(135deg,#ece8df,#e3dccb 50%,#efe9d9)}
.location-title{position:absolute;left:382px;top:21px;font-family:"Ubuntu",sans-serif;font-weight:500;font-size:23px;color:#7a9e00;letter-spacing:.5px}
.location-copy{position:absolute;left:384px;top:58px;width:242px;font-size:11.5px;line-height:20px;text-align:justify}
.postcode-label{position:absolute;left:382px;top:224px;font-size:12.5px;color:#333}
.postcode{position:absolute;left:523px;top:220px;width:102px;height:23px;border:1px solid #ccc;background:#fff;font-size:10px;color:#888;padding:5px 8px}
.search-btn{position:absolute;left:597px;top:249px}

/* quote */
.quote{position:absolute;left:728px;top:838px;width:303px;height:300px;border-radius:16px;background:var(--lime-deep);overflow:hidden;font-family:"Ubuntu",sans-serif;color:#fff}
.quote-head{height:38px;background:linear-gradient(var(--lime),var(--lime-deep));padding:7px 26px;font-weight:500;font-size:19px}
.quote-row{position:absolute;left:0;width:303px;height:20px;font-size:13px}
.quote-row span{position:absolute;right:222px;top:1px}
.spin{position:absolute;left:85px;top:0;width:147px;height:19px;background:#fff;border:1px solid #aaa}
.spin::after{content:"";position:absolute;right:0;top:0;width:12px;height:17px;border-left:1px solid #ccc;background:linear-gradient(#eee,#ccc)}
.check{position:absolute;left:56px;width:23px;height:18px;background:linear-gradient(#fff,#ddd);border:1px solid #aaa}
.check-label{position:absolute;left:89px;font-size:13px}
.estimate-label{position:absolute;left:17px;top:199px;font-weight:500;font-size:13px}
.estimate{position:absolute;left:18px;top:220px;width:243px;height:23px;background:#fff;border:1px solid #777}
.btn-learn{position:absolute;left:188px;top:259px;width:88px;height:23px;border-radius:12px;background:linear-gradient(#555,#1b1b1b);font-size:12px;text-align:center;line-height:23px}

/* footer */
.site-footer{position:absolute;left:0;top:1153px;width:1100px;height:47px;background:linear-gradient(#555,#333);color:#fff;font-size:12px;letter-spacing:.6px}
.footer-nav{position:absolute;top:8px;left:0;width:1100px;text-align:center;white-space:nowrap}
.footer-nav a{color:#fff;text-decoration:none}
.footer-nav i{font-style:normal;margin:0 17px}
.copyright{position:absolute;top:28px;width:1100px;text-align:center}
</style>
</head>
<body>

<header class="site-header">
  <div class="brand"><span>Orvane Lux</span><span class="brand-dot"></span></div>
  <div class="callout">
    <span class="callout-icon"></span>
    <span class="callout-label">Call us Today</span>
    <span class="callout-phone">555-0142-7730</span>
  </div>
  <nav class="main-nav">
    <a class="active" href="#" style="left:566px;width:60px">HOME</a>
    <a href="#" style="left:650px;width:80px">ABOUT US</a>
    <a href="#" style="left:766px;width:76px">SERVICES</a>
    <a href="#" style="left:870px;width:68px">WHY US</a>
    <a href="#" style="left:970px;width:72px">CONTACT</a>
  </nav>
</header>

<section class="hero">
  <div class="hero-frame"><div class="hero-photo" role="img" aria-label="Business people standing on rising grey columns, one on a green block"></div></div>
  <h1 class="hero-title">Hello!</h1>
  <p class="hero-copy">Lorem ipsum dolor sit consectetuer adipiscing Praesent vestibulum aenean nonummyhendrerit mauris. Hasellus porta aenean nonummyhendrerit mauris aenean nonummyhendrerit mauris. Hasellus porta. Fusce suscipit varius mi. Cum sociis natoque penatibus et magnis dis parturient.</p>
  <div class="btn-more">MORE INFO</div>
</section>
<div class="hero-rule"></div>

<article class="service" style="left:63px">
  <h2 class="service-head">ZOB</h2>
  <span class="service-icon" style="background:radial-gradient(circle at 40% 35%,#9bd3ff,#1b6fc4)"></span>
  <div class="service-photo"><div role="img" aria-label="Row of smartphones"></div></div>
  <div class="service-copy">
    <p>We have over 50 combined years in supporting Zobline systems.</p>
    <p>Our Zobline specialists speak plain English so you're not left baffled by computer jargon.</p>
    <ul class="service-list"><li>SME &amp; Corporate Networks</li><li>Kestra Email Server</li><li>Bespoke Applications</li><li>Web Services</li><li>Connectivity</li><li>Security</li></ul>
  </div>
</article>

<article class="service" style="left:394px">
  <h2 class="service-head">PC</h2>
  <span class="service-icon" style="border-radius:4px;background:linear-gradient(#6fb6f0,#1a5fa8)"></span>
  <div class="service-photo"><div role="img" aria-label="Desktop computers, tower and laptops"></div></div>
  <div class="service-copy">
    <p>Friendly Windrow techs with years of industry experience.</p>
    <p>Friendly Windrow techs with years of industry experience.</p>
    <ul class="service-list"><li>SME &amp; Corporate Networks</li><li>Kestra Email Server</li><li>Bespoke Applications</li><li>Web Services</li><li>Connectivity</li><li>Security</li></ul>
  </div>
</article>

<article class="service" style="left:725px">
  <h2 class="service-head">Combined</h2>
  <span class="service-icon" style="border-radius:4px;background:linear-gradient(#8fd0ff,#2066b5)"></span>
  <div class="service-photo"><div role="img" aria-label="Tablets and phones from several makers"></div></div>
  <div class="service-copy">
    <p>Using both Zobs &amp; PC's can be tricky but not with us.</p><br>
    <p>Orvane is a joint venture between two IT directors, one Zob focused and one PC focused but both with proven track records in running successful IT supports firms.</p><br>
    <p>Our engineers are specialists not all rounders. This means you get the correct fix not a hack.Our engineers are specialists not all rounders. This means you get the correct fix not a hack.</p>
  </div>
</article>

<section class="location">
  <div class="map" role="img" aria-label="Street map of Soho and Covent Garden with the office marked"></div>
  <h2 class="location-title">Location</h2>
  <p class="location-copy">This map shows where we are, smack bang in the middle of Soho and Covent Garden. Type your postcode in to see how close we are to your offices. map shows where we are, smack bang in the middle of Soho and Covent Garden. Type your postcode in to see how close we are to your offices.</p>
  <span class="postcode-label">Enter your post code :</span>
  <div class="postcode">W1X 0ZZ</div>
  <svg class="search-btn" width="30" height="30" viewBox="0 0 30 30" aria-label="Search">
    <circle cx="15" cy="15" r="14" fill="#7ab800"/>
    <circle cx="13" cy="13" r="6" fill="none" stroke="#fff" stroke-width="2.5"/>
    <line x1="17.5" y1="17.5" x2="22" y2="22" stroke="#fff" stroke-width="3" stroke-linecap="round"/>
  </svg>
</section>

<aside class="quote">
  <div class="quote-head">Insti-Quote</div>
  <div class="quote-row" style="top:47px"><span>Laptops :</span><div class="spin"></div></div>
  <div class="quote-row" style="top:73px"><span>Desktops :</span><div class="spin"></div></div>
  <div class="quote-row" style="top:99px"><span>Servers :</span><div class="spin"></div></div>
  <span class="check" style="top:137px"></span><span class="check-label" style="top:137px">Remote support</span>
  <span class="check" style="top:163px"></span><span class="check-label" style="top:164px">Server Monitoring</span>
  <span class="estimate-label">Monthly Estimate :</span>
  <div class="estimate"></div>
  <div class="btn-learn">Learn More</div>
</aside>

<footer class="site-footer">
  <nav class="footer-nav"><a href="#">Home</a><i>|</i><a href="#">About Us</a><i>|</i><a href="#">Services</a><i>|</i><a href="#">Why Us</a><i>|</i><a href="#">Contact</a></nav>
  <div class="copyright">© Orvane Lux Ltd 2011</div>
</footer>

</body>
</html>
```